Publisher needs a book cover design for ‘Quiet Harm at the Chalkboard’ book

We need a book cover (front, back, spine) for the 2nd edition of a book entitled ‘Quiet Harm at the Chalkboard’ and subtitled ‘the overlooked layer of pupil welfare, youth security and careful hiring practice’ (inverted commas not to be part of the title and subtitle). The author is Malcolm Pettifer. The publisher is Wendlebury Press. The finished size of the paperback version will be the industry standard 9" x 6". There will be paperback, hardback, and e-book versions. The final number of pages is expected to be in the region 150-180 pages. Text for the back cover is not yet available, but at the bottom of the back cover should be publisher logo (rectangular) on the left and space for the ISBN bar code on the right. The circular logo should be on the spine. The design should be original and not include any stock images that have been created by someone else or may require obtaining a copyright licence to use. Symbols in common use and not copyrighted are probably ok. There are no required images, photographs or symbols except the publisher logo at the left bottom of the back cover and lower spine. Spine lettering should be UK/US style with the top of the writing nearest the front cover. The designer is free to be creative using appropriate diagrams, symbols or abstract designs. Rectangular and circular variants of the publisher logo are attached. Designers are assured that when evaluating designs absolutely no notice whatsoever is taken of a designer's Pixel Guild ranking or status; We are completely output driven, so what matters is the design, not the ranking or status of the designer. In a similar way, designs are not evaluated as 'good' or 'bad' - the winning design will be chosen after review by a design review panel and is not decided arbitrarily by a single person. All submitted designs should be capable of effective copyright assignment.

Target Market(s)

Practitioners, parents, teachers, pupils and academics concerned with child protection, safeguarding and the elimination of emotional abuse of children in the classroom

Font styles to use
Serif
Sans Serif

Requirements
Must have
• • Title, author, edition, subtitle, publisher logo
Nice to have
• • Originality, innovation
Should not have
• • Stock images or anything else requiring additional copyright discussions and negotiations.

```html
<!DOCTYPE html>
<html lang="en">
<head>
<meta charset="utf-8">
<title>Quiet Harm at the Chalkboard — Cover</title>
<link rel="stylesheet" href="https://fonts.googleapis.com/css2?family=Bodoni+Moda:wght@400;700&family=Libre+Bodoni:wght@400;700&display=swap">
<style>
  :root {
    --maroon: #772433;
    --maroon-deep: #5e1a27;
    --rose-light: #e8b9ad;
    --white: #ffffff;
    --display: "Bodoni Moda", serif;
    --text: "Libre Bodoni", serif;
  }
  html, body { margin: 0; padding: 0; overflow: hidden; background: var(--maroon); }
  .cover {
    position: relative;
    width: 1200px;
    height: 880px;
    background: var(--maroon);
    color: var(--white);
    overflow: hidden;
  }

  /* Back cover */
  .back { position: absolute; left: 0; top: 0; width: 580px; height: 880px; }
  .back-title {
    position: absolute; left: 48px; top: 20px; margin: 0;
    font-family: var(--display); font-weight: 400;
    font-size: 68px; line-height: 67px;
  }
  .back-blurb {
    position: absolute; left: 45px; top: 280px; width: 510px; margin: 0;
    font-family: var(--display); font-weight: 400;
    font-size: 17px; line-height: 26.7px;
    text-align: justify; hyphens: auto;
  }
  .imprint {
    position: absolute; left: 45px; top: 776px;
    display: flex; align-items: center; gap: 8px;
    font-family: var(--text); font-size: 21px; letter-spacing: 0.5px;
  }
  .imprint-dot { width: 46px; height: 46px; border-radius: 50%; background: var(--white); }
  .isbn-space {
    position: absolute; left: 367px; top: 728px; width: 193px; height: 116px;
    background: var(--white);
  }

  /* Spine */
  .spine { position: absolute; left: 582px; top: 0; width: 34px; height: 880px; }
  .spine-line {
    position: absolute; left: 0; width: 34px;
    writing-mode: vertical-rl; line-height: 34px;
    white-space: nowrap; text-align: start;
  }
  .spine-title { top: 46px; font-family: var(--display); font-size: 26px; }
  .spine-edition { top: 446px; font-family: var(--text); font-size: 13px; letter-spacing: 0.3px; }
  .spine-author { top: 624px; font-family: var(--text); font-weight: 700; font-size: 18px; }
  .spine-mark {
    position: absolute; left: 4px; top: 797px; width: 26px; height: 26px;
    border-radius: 50%; background: var(--white);
  }

  /* Front cover */
  .front { position: absolute; left: 616px; top: 0; width: 584px; height: 880px; }
  .front-scene {
    position: absolute; inset: 0;
    background:
      radial-gradient(ellipse 260px 110px at 250px 90px, rgba(240,200,190,0.85), transparent 75%),
      linear-gradient(180deg, #8e3a45 0%, #a9505a 35%, #8d3b46 60%, var(--maroon) 100%);
  }
  .front-title {
    position: absolute; left: 24px; top: 352px; margin: 0;
    font-family: var(--display); font-weight: 400;
    font-size: 74px; line-height: 72px;
  }
  .front-subtitle {
    position: absolute; left: 24px; top: 598px; width: 460px; margin: 0;
    font-family: var(--text); font-size: 21px; line-height: 26px;
  }
  .front-edition {
    position: absolute; left: 24px; top: 694px; margin: 0;
    font-family: var(--text); font-size: 19px;
  }
  .front-author {
    position: absolute; left: 24px; top: 792px; margin: 0;
    font-family: var(--text); font-weight: 700; font-size: 26px;
  }
</style>
</head>
<body>
<main class="cover">
  <section class="back">
    <h2 class="back-title">Quiet Harm<br>at the<br>Chalkboard</h2>
    <p class="back-blurb">Lorem Ipsum is simply dummy text of the printing and typesetting industry. Lorem Ipsum has been the industry's standard dummy text ever since the 1500s, when an unknown printer took a galley of type and scrambled it to make a type specimen book. It has survived not only five centuries, but also the leap into electronic typesetting, remaining essentially unchanged. It was popularised in the 1960s with the release of Letraset sheets containing Lorem Ipsum passages, and more recently with desktop publishing software like Aldus PageMaker including versions of Lorem Ipsum.</p>
    <div class="imprint"><span class="imprint-dot"></span><span>WENDLEBURY PRESS</span></div>
    <div class="isbn-space"></div>
  </section>

  <section class="spine">
    <span class="spine-line spine-title">Quiet Harm at the Chalkboard</span>
    <span class="spine-line spine-edition">2ND EDITION</span>
    <span class="spine-line spine-author">Malcolm Pettifer</span>
    <span class="spine-mark"></span>
  </section>

  <section class="front">
    <div class="front-scene" role="img" aria-label="Tinted photograph of an empty classroom with a board, teacher's desk and rows of pupil desks"></div>
    <h1 class="front-title">Quiet Harm<br>at the<br>Chalkboard</h1>
    <p class="front-subtitle">the overlooked layer of pupil welfare, youth security and careful hiring practice</p>
    <p class="front-edition">2ND EDITION</p>
    <p class="front-author">Malcolm Pettifer</p>
  </section>
</main>
</body>
</html>
```